New Zealand Luggage Importer Needs Business Cards

We need professional, creative and fashionable business cards created.
We are based in New Zealand and import and distribute high-end, quality, fashionable and durable luggage.
We pride ourselves on selling the very best quality luggage, second only to 1 brand (which we won't mention here)...we use the same manufacturer. However, our prices are much more reasonable.
Industry/Entity Type
Business
Contact Information for Business Card
Mark Dunsley
027 512 4068
3/17 Harlow Street, Pinecrest Flats, Auckland, 0614
PO Box 204377, Fernside, Auckland 0731
09-528-3916
sales@brivancases.co.nz / www.brivancases.co.nz

```html
<!DOCTYPE html>
<html lang="en">
<head>
<meta charset="utf-8">
<title>Brivan Cases – Business Cards</title>
<link href="https://fonts.googleapis.com/css2?family=Quicksand:wght@400;500;600&display=swap" rel="stylesheet">
<style>
  :root {
    --backdrop: #3a3a3c;
    --card: #0d0d0d;
    --band: #050505;
    --gold: #c9a24a;
    --white: #f2f2f2;
    --rule: #2a2a2a;
    --silver: #9a9a9a;
  }
  * { margin: 0; padding: 0; box-sizing: border-box; }
  html, body { width: 1200px; height: 1000px; overflow: hidden; }
  body {
    background: var(--backdrop);
    font-family: "Quicksand", sans-serif;
    position: relative;
  }
  .card {
    position: absolute;
    left: 280px;
    width: 640px;
    height: 366px;
    background: var(--card);
    border-radius: 22px;
    overflow: hidden;
    box-shadow: 0 18px 40px rgba(0,0,0,0.45);
  }
  .card-front { top: 100px; }
  .card-back { top: 534px; }

  .front-band {
    position: absolute;
    left: 0; right: 0;
    top: 128px;
    height: 110px;
    background: var(--band);
    display: flex;
    align-items: center;
    justify-content: center;
  }
  .brand-name {
    font-family: "Quicksand", sans-serif;
    font-weight: 600;
    color: var(--gold);
    letter-spacing: 3px;
    white-space: nowrap;
  }
  .front-band .brand-name { font-size: 46px; }

  .back-brand {
    position: absolute;
    left: 0; top: 0;
    width: 290px; height: 100%;
    display: flex;
    align-items: center;
    justify-content: center;
  }
  .back-brand .brand-name { font-size: 30px; }

  .divider-band {
    position: absolute;
    left: 290px; top: 0;
    width: 48px; height: 100%;
  }
  .contact {
    position: absolute;
    left: 356px; top: 40px;
    width: 260px;
  }
  .contact-name {
    color: var(--white);
    font-size: 24px;
    font-weight: 500;
    margin-bottom: 14px;
  }
  .contact-line {
    color: var(--gold);
    font-size: 13px;
    line-height: 18px;
    padding: 7px 0;
    border-top: 1px solid var(--rule);
  }
</style>
</head>
<body>

<section class="card card-front">
  <div class="front-band">
    <span class="brand-name">BRIVAN CASES</span>
  </div>
</section>

<section class="card card-back">
  <div class="back-brand">
    <span class="brand-name">BRIVAN CASES</span>
  </div>

  <svg class="divider-band" viewBox="0 0 48 366" width="48" height="366" aria-hidden="true">
    <rect x="0" y="0" width="48" height="366" fill="var(--band)"/>
    <rect x="0" y="0" width="2" height="366" fill="var(--silver)"/>
    <!-- phone -->
    <path d="M18 86 q-3 6 3 12 q6 6 12 3 l-3-4 q-3 2 -6-1 q-3-3 -1-6 z" fill="var(--gold)"/>
    <!-- mail -->
    <rect x="15" y="124" width="20" height="14" fill="none" stroke="var(--gold)" stroke-width="2"/>
    <path d="M15 124 l10 8 l10 -8" fill="none" stroke="var(--gold)" stroke-width="2"/>
    <!-- pin -->
    <path d="M25 172 c-6 0 -9 4 -9 8 c0 6 9 14 9 14 c0 0 9 -8 9 -14 c0 -4 -3 -8 -9 -8 z" fill="var(--gold)"/>
    <circle cx="25" cy="180" r="3" fill="var(--band)"/>
    <!-- pin -->
    <path d="M25 222 c-6 0 -9 4 -9 8 c0 6 9 14 9 14 c0 0 9 -8 9 -14 c0 -4 -3 -8 -9 -8 z" fill="var(--gold)"/>
    <circle cx="25" cy="230" r="3" fill="var(--band)"/>
    <!-- monitor -->
    <rect x="14" y="272" width="22" height="15" fill="none" stroke="var(--gold)" stroke-width="2"/>
    <path d="M21 292 h8 M25 287 v5" stroke="var(--gold)" stroke-width="2"/>
  </svg>

  <div class="contact">
    <p class="contact-name">Mark Dunsley</p>
    <p class="contact-line">027 512 4068 | 09-528-3916</p>
    <p class="contact-line">sales@brivancases.co.nz</p>
    <p class="contact-line">3/17 Harlow Street, Pinecrest Flats,<br>Auckland, 0614</p>
    <p class="contact-line">PO Box 204377, Fernside,<br>Auckland 0731</p>
    <p class="contact-line">www.brivancases.co.nz</p>
  </div>
</section>

</body>
</html>
```